GP doctor business card to give to patients existing logo or modification & clinic times

Use new colours of logo Sage green, buttercup yellow. Uploading PREVIOUS card. 1)Front information - Dr Lucan Merivale MBBS, FRACGP, Family General Practitioner, Caring for your health, www.drmerivalegp.example and new logo or modification of logo of Merivale Family Medical Practice. Use new colours of logo on white background. Remove dark background from logo.
2)Back of card - Mon - Thurs - 7 am - 7 pm. Friday 8 am - 5 pm Saturday - 1 pm - 5 pm. Use BookWell application or website to make appointments. Space to write appointment times. New address Suite 4, 82 Parnell Avenue, Ashgrove Vale - 2768. Phone 1300 417 829 Fax 02 8156 4271

Target Market(s)

Patients

Contact Information for Business Card

As above

Requirements
Must have
• As above

```html
<!DOCTYPE html>
<html lang="en">
<head>
<meta charset="utf-8">
<title>Merivale Family Medical Practice – Business Card</title>
<link href="https://fonts.googleapis.com/css2?family=Poppins:wght@400;500;600&display=swap" rel="stylesheet">
<style>
  :root {
    --sage: #86a383;
    --buttercup: #f8f4b4;
    --ink: #404040;
    --white: #ffffff;
    --backdrop: #2b2b2b;
    --ghost: #f4f4f4;
  }
  * { box-sizing: border-box; margin: 0; padding: 0; }
  html, body {
    width: 1200px; height: 900px; overflow: hidden;
    background: var(--backdrop);
    font-family: "Poppins", sans-serif;
  }
  .card {
    position: absolute; left: 250px;
    width: 700px; height: 400px;
    border-radius: 26px; overflow: hidden;
    box-shadow: 0 12px 30px rgba(0,0,0,.45);
  }

  /* ---------- Back ---------- */
  .card-back { top: 36px; background: var(--sage); color: var(--white); }
  .back-info {
    position: absolute; top: 48px; left: 0; right: 0;
    display: flex; justify-content: center; align-items: center; gap: 26px;
  }
  .hours { color: var(--buttercup); font-size: 21px; font-weight: 500; line-height: 1.45; text-align: right; }
  .divider { width: 2px; height: 96px; background: var(--buttercup); }
  .contacts { list-style: none; font-size: 19px; font-weight: 500; line-height: 1.6; }
  .contacts li { display: flex; align-items: center; gap: 10px; }
  .contact-icon {
    width: 26px; height: 26px; border-radius: 50%;
    background: var(--buttercup); display: flex; align-items: center; justify-content: center;
  }
  .contact-icon svg { width: 15px; height: 15px; }
  .address { position: absolute; top: 176px; width: 100%; text-align: center; font-size: 18px; font-weight: 500; }
  .appointment-box {
    position: absolute; top: 222px; left: 64px; right: 64px; height: 100px;
    background: var(--white); border-radius: 50px; overflow: hidden;
  }
  .appointment-label {
    height: 30px; background: var(--buttercup); color: var(--sage);
    font-size: 14px; font-weight: 500; text-align: center; line-height: 30px;
  }
  .ampm { position: absolute; right: 60px; top: 6px; color: var(--sage); font-size: 12px; font-weight: 500; }
  .booking-note { position: absolute; top: 340px; width: 100%; text-align: center; font-size: 18px; font-weight: 500; }

  /* ---------- Front ---------- */
  .card-front { top: 470px; background: var(--white); }
  .ghost-mark {
    position: absolute; right: -20px; top: -40px; width: 280px; height: 280px;
    border-radius: 50%; background: var(--ghost);
  }
  .practice-lockup { position: absolute; left: 40px; top: 48px; display: flex; align-items: center; gap: 16px; }
  .lockup-dot { width: 84px; height: 84px; border-radius: 50%; background: var(--sage); flex: none; }
  .practice-name {
    color: var(--sage); font-weight: 500; font-size: 24px; line-height: 1.25; letter-spacing: 1px;
    text-transform: uppercase;
  }
  .practice-rule { position: absolute; left: 40px; top: 150px; width: 380px; height: 2px; background: var(--sage); }
  .tagline-block { position: absolute; right: 40px; top: 160px; text-align: right; }
  .tagline { color: var(--sage); font-size: 20px; }
  .tagline-rule { height: 2px; background: var(--sage); margin: 4px 0 6px auto; width: 400px; }
  .website { color: var(--sage); font-size: 19px; font-weight: 600; }
  .doctor { position: absolute; left: 40px; top: 250px; }
  .doctor-name { color: var(--ink); font-size: 24px; font-weight: 600; }
  .doctor-meta { color: var(--sage); font-size: 20px; line-height: 1.35; }
  .doctor-rule { position: absolute; left: 310px; top: 268px; width: 170px; height: 2px; background: var(--sage); }
  .front-band {
    position: absolute; left: 0; right: 0; bottom: 0; height: 18px;
    background: linear-gradient(90deg, var(--sage) 0%, var(--sage) 35%, var(--buttercup) 100%);
  }
</style>
</head>
<body>

<section class="card card-back" aria-label="Card back">
  <div class="back-info">
    <div class="hours">
      <p>Mon - Thurs : 7 am - 7 pm</p>
      <p>Friday : 8 am - 5 pm</p>
      <p>Saturday : 1 pm - 5 pm</p>
    </div>
    <div class="divider"></div>
    <ul class="contacts">
      <li><span class="contact-icon"><svg viewBox="0 0 24 24"><path fill="#86a383" d="M6.6 10.8a15 15 0 0 0 6.6 6.6l2.2-2.2a1 1 0 0 1 1-.25 11.4 11.4 0 0 0 3.6.57 1 1 0 0 1 1 1V20a1 1 0 0 1-1 1A17 17 0 0 1 3 4a1 1 0 0 1 1-1h3.5a1 1 0 0 1 1 1c0 1.25.2 2.45.57 3.57a1 1 0 0 1-.25 1z"/></svg></span>1300 417 829</li>
      <li><span class="contact-icon"><svg viewBox="0 0 24 24"><path fill="#86a383" d="M6 3h12v5H6zM4 9h16a2 2 0 0 1 2 2v6h-4v4H6v-4H2v-6a2 2 0 0 1 2-2zm4 7v3h8v-3z"/></svg></span>02 8156 4271</li>
      <li><span class="contact-icon"><svg viewBox="0 0 24 24"><path fill="#86a383" d="M12 2a7 7 0 0 0-7 7c0 5 7 13 7 13s7-8 7-13a7 7 0 0 0-7-7zm0 9.5A2.5 2.5 0 1 1 12 6.5a2.5 2.5 0 0 1 0 5z"/></svg></span>www.drmerivalegp.example</li>
    </ul>
  </div>
  <p class="address">Suite 4, 82 Parnell Avenue, Ashgrove Vale - 2768.</p>
  <div class="appointment-box">
    <div class="appointment-label">Appointment Time</div>
    <span class="ampm">AM | PM</span>
  </div>
  <p class="booking-note">Use BookWell application or website to make appointments.</p>
</section>

<section class="card card-front" aria-label="Card front">
  <div class="ghost-mark"></div>
  <div class="practice-lockup">
    <span class="lockup-dot"></span>
    <p class="practice-name">Merivale<br>Family Medical Practice</p>
  </div>
  <div class="practice-rule"></div>
  <div class="tagline-block">
    <p class="tagline">Caring for your health</p>
    <div class="tagline-rule"></div>
    <p class="website">WWW.DRMERIVALEGP.EXAMPLE</p>
  </div>
  <div class="doctor">
    <p class="doctor-name">DR LUCAN MERIVALE</p>
    <p class="doctor-meta">MBBS, FRACGP</p>
    <p class="doctor-meta">Family General Practitioner</p>
  </div>
  <div class="doctor-rule"></div>
  <div class="front-band"></div>
</section>

</body>
</html>
```